Fact Sheets for Insurance

We need a 4 page booklet brochure designed for our insurance business. Each page is A4. We design insurance plans for our Clients and we wish to use the brochure to market and educate our Client and business partners. The business is Halvard Mensley Financial Services. Colour scheme of our logo and stationary is navy blue and metallic gold. The content has been drafted and each page is attached. Please use your creative freedom to make it look professional and modern. We would like graphics, pictures etc to make it more vibrant as well.

Industry/Entity Type

Insurance

```html
<!DOCTYPE html>
<html lang="en">
<head>
<meta charset="utf-8">
<title>Insurance Fact Sheets – Halvard Mensley Financial Services</title>
<link href="https://fonts.googleapis.com/css2?family=Open+Sans:ital,wght@0,400;0,600;0,700;1,400;1,600&family=Exo+2:ital,wght@1,900&family=Cormorant+Garamond:wght@500&display=swap" rel="stylesheet">
<style>
:root{
  --backdrop:#c4c4c4;
  --navy:#1f3d6d;
  --gold:#a89a6c;
  --gold-light:#c9b98a;
  --ink:#2d2d2d;
  --white:#ffffff;
  --cell-head:#c6c6c6;
  --cell:#e3e3e3;
}
*{box-sizing:border-box;margin:0;padding:0}
html,body{width:1200px;height:1000px;overflow:hidden;background:var(--backdrop)}
body{position:relative;font-family:"Open Sans",Arial,sans-serif;color:var(--white)}

.sheet{position:absolute;width:684px;height:968px;background:var(--navy);overflow:hidden}
.sheet--main{left:122px;top:15px}
.sheet--thumb{transform:scale(.3246);transform-origin:0 0;left:853px}
.sheet--tpd{top:15px}
.sheet--income{top:339px}
.sheet--critical{top:666px}

.sheet__title{position:absolute;top:28px;left:0;width:684px;text-align:center;font-size:24px;font-weight:700;letter-spacing:.2px}
.banner{position:absolute;left:33px;top:80px;width:619px;height:149px;border:3px solid var(--gold);overflow:hidden}
.banner__photo{position:absolute;inset:0}
.banner__tag{position:absolute;right:30px;bottom:6px;font-family:"Exo 2",sans-serif;font-style:italic;font-weight:900;font-size:31px;line-height:30px;color:var(--navy);letter-spacing:1px}

.board{position:absolute;left:31px;top:250px;width:622px;height:557px;background:var(--gold)}
.board__head{position:absolute;height:27px;line-height:27px;text-align:center;font-size:14px;font-weight:600;color:var(--ink)}
.board__panel{position:absolute;background:var(--navy);overflow:hidden}
.col-left{left:5px;width:304px}
.col-right{left:314px;width:303px}
.row-1h{top:3px}
.row-1p{top:31px;height:156px}
.row-2h{top:191px}
.row-2p{top:221px;height:332px}

.need-table{position:absolute;left:9px;top:14px;width:287px;border-collapse:collapse;font-size:12px;color:var(--ink)}
.need-table th{background:var(--cell-head);font-weight:600;height:22px;border:2px solid var(--white)}
.need-table td{background:var(--cell);height:20px;border:2px solid var(--white);padding-left:12px;white-space:nowrap}
.need-table td.amount{width:144px;padding-left:8px}
.need-table tr.total td:first-child{text-align:right;padding-right:10px;font-weight:700}

.dot-list{list-style:none;position:absolute;left:12px;top:10px;right:10px;font-size:13px}
.dot-list li{position:relative;padding-left:14px;line-height:18px;margin-bottom:10px}
.dot-list li::before{content:"";position:absolute;left:0;top:6px;width:7px;height:7px;border-radius:50%;background:var(--gold-light)}
.dot-list--advice{top:42px}
.dot-list--advice li{margin-bottom:5px}

.tick-list{list-style:none;position:absolute;left:12px;top:12px;right:10px;font-size:12.8px;line-height:16px}
.tick-list li{position:relative;padding-left:30px;margin-bottom:9px;text-align:justify}
.tick-list svg{position:absolute;left:2px;top:1px;width:16px;height:14px}
.tick-list b{font-weight:700}
.spaced{letter-spacing:1.8px}

.panel-copy{position:absolute;left:12px;right:12px;font-size:13px;line-height:17px}

.sheet--thumb .tick-list{font-size:11.5px;line-height:14.5px}
.sheet--thumb .tick-list li{margin-bottom:7px}
.sheet--thumb .dot-list{font-size:12px}
.sheet--thumb .panel-copy{font-size:12px;line-height:15px}
.sheet--income .tick-list{font-size:10.6px;line-height:13.2px;top:8px}
.sheet--income .tick-list li{margin-bottom:5px}
.sheet--income .dot-list--advice li{margin-bottom:3px;line-height:16px}

.disclaimer{position:absolute;left:32px;top:812px;width:624px;font-size:9.2px;line-height:13px;font-style:italic;font-weight:600}
.brand{position:absolute;left:0;top:880px;width:684px;text-align:center;font-family:"Cormorant Garamond",serif;font-weight:500;color:var(--white);font-size:17px;line-height:20px;letter-spacing:1.5px}
.brand__mark{display:block;width:22px;height:22px;margin:0 auto 8px;background:var(--gold)}
</style>
</head>
<body>

<section class="sheet sheet--main">
  <h1 class="sheet__title">Buying Life Insurance</h1>
  <div class="banner">
    <div class="banner__photo" role="img" aria-label="Photo of a smiling family of four lying close together" style="background:linear-gradient(90deg,#c9a98a 0%,#e8cdb4 30%,#f3ddc6 55%,#ffffff 58%,#ffffff 100%)"></div>
    <div class="banner__tag">LIFE<br>INSURANCE!</div>
  </div>

  <div class="board">
    <div class="board__head col-left row-1h">How Much Do I Need?</div>
    <div class="board__head col-right row-1h">Who Offers It?</div>
    <div class="board__panel col-left row-1p">
      <table class="need-table">
        <tr><th>Need</th><th>Amount</th></tr>
        <tr><td>Repaying Debts</td><td class="amount">$</td></tr>
        <tr><td>Funeral Expenses</td><td class="amount">$</td></tr>
        <tr><td>Replacing your income</td><td class="amount">$</td></tr>
        <tr><td>Others</td><td class="amount">$</td></tr>
        <tr class="total"><td>Total</td><td class="amount">$</td></tr>
      </table>
    </div>
    <div class="board__panel col-right row-1p">
      <ul class="dot-list">
        <li>Most Superannuation Funds</li>
        <li>Some Private Health Funds</li>
        <li>Some Employers</li>
        <li>Life Insurance Companies</li>
        <li>General Insurance Companies</li>
      </ul>
    </div>

    <div class="board__head col-left row-2h">Tips and Traps</div>
    <div class="board__head col-right row-2h">When to Call a Professional Advisor?</div>
    <div class="board__panel col-left row-2p">
      <ul class="tick-list">
        <li><svg viewBox="0 0 16 14"><path d="M1 7l5 5L15 1" fill="none" stroke="#a89a6c" stroke-width="2.4"/></svg>Ensure contract <b>covers all causes of death,</b> not just accidents.</li>
        <li><svg viewBox="0 0 16 14"><path d="M1 7l5 5L15 1" fill="none" stroke="#a89a6c" stroke-width="2.4"/></svg><b>Review exclusions</b>. The only standard industry exclusion is "suicide within first 13 <span class="spaced">months of policy inception or</span> reinstatement".</li>
        <li><svg viewBox="0 0 16 14"><path d="M1 7l5 5L15 1" fill="none" stroke="#a89a6c" stroke-width="2.4"/></svg>Look to <b>purchase "Long Term" Life Insurance</b> if you think you will need to hold the policy for a number of years. This may save you tens of thousands of dollars over the life of your policy.</li>
        <li><svg viewBox="0 0 16 14"><path d="M1 7l5 5L15 1" fill="none" stroke="#a89a6c" stroke-width="2.4"/></svg>Ensure the contract is <b>guaranteed to be renewed</b> if you pay your premiums until expiry age.</li>
        <li><svg viewBox="0 0 16 14"><path d="M1 7l5 5L15 1" fill="none" stroke="#a89a6c" stroke-width="2.4"/></svg>If purchased through Super, your <b>beneficiaries may be liable for a tax bill</b> in the event of a claim</li>
      </ul>
    </div>
    <div class="board__panel col-right row-2p">
      <p class="panel-copy" style="top:12px">If you need help:</p>
      <ul class="dot-list dot-list--advice">
        <li>Comparing premiums or policies</li>
        <li>Reviewing wording of insurance contacts</li>
        <li>Structuring your policies to get a tax deduction</li>
        <li>Avoiding tax on claim proceeds</li>
        <li>Purchasing “Long Term” Life Insurance</li>
      </ul>
      <p class="panel-copy" style="top:186px">If you want to ensure that you have someone assisting your family if a claim is ever needed to be made</p>
    </div>
  </div>

  <p class="disclaimer">The information provided on this Fact Sheet is <b>general advice only</b> so does <b>not</b> take into account your objective, financial situation and needs. Before acting on any information contained on this Fact Sheet you should consider the appropriateness of the advice having regard to your own objectives, financial situation and needs.</p>
  <div class="brand"><span class="brand__mark"></span>HALVARD MENSLEY<br>FINANCIAL SERVICES</div>
</section>

<section class="sheet sheet--thumb sheet--tpd">
  <h1 class="sheet__title">Buying Total &amp; Permanent Disability (TPD) Insurance</h1>
  <div class="banner">
    <div class="banner__photo" role="img" aria-label="Photo of a hand on a wheelchair wheel" style="background:linear-gradient(90deg,#e9e9e9 0%,#7a7a7a 35%,#2a2a2a 60%,#bdbdbd 100%)"></div>
  </div>
  <div class="board">
    <div class="board__head col-left row-1h">How Much Do I Need?</div>
    <div class="board__head col-right row-1h">Who Offers It?</div>
    <div class="board__panel col-left row-1p">
      <table class="need-table">
        <tr><th>Need</th><th>Amount</th></tr>
        <tr><td>Repaying Debts</td><td class="amount">$</td></tr>
        <tr><td>Medical Expenses</td><td class="amount">$</td></tr>
        <tr><td>Home Modification Costs</td><td class="amount">$</td></tr>
        <tr><td>Others</td><td class="amount">$</td></tr>
        <tr class="total"><td>Total</td><td class="amount">$</td></tr>
      </table>
    </div>
    <div class="board__panel col-right row-1p">
      <ul class="dot-list">
        <li>Most Superannuation Funds</li>
        <li>Some Private Health Funds</li>
        <li>Some Employers</li>
        <li>Life Insurance Companies</li>
        <li>General Insurance Companies</li>
      </ul>
    </div>
    <div class="board__head col-left row-2h">Tips and Traps</div>
    <div class="board__head col-right row-2h">When to Call a Professional Advisor?</div>
    <div class="board__panel col-left row-2p">
      <ul class="tick-list">
        <li><svg viewBox="0 0 16 14"><path d="M1 7l5 5L15 1" fill="none" stroke="#a89a6c" stroke-width="2.4"/></svg><b>Purchase an "Own Occupation" definition Policy</b> to ensure that you are not tested against your ability to work in "Any Occupation" at claim time.</li>
        <li><svg viewBox="0 0 16 14"><path d="M1 7l5 5L15 1" fill="none" stroke="#a89a6c" stroke-width="2.4"/></svg><b>Review what the policy doesn't cover "Exclusions"</b>. Standard exclusion for most policies is self inflicted acts.</li>
        <li><svg viewBox="0 0 16 14"><path d="M1 7l5 5L15 1" fill="none" stroke="#a89a6c" stroke-width="2.4"/></svg>Look to <b>purchase "Long Term" Life Insurance</b> if you think you will need to hold the policy for a number of years. This may save you tens of thousands of dollars over the life of your policy.</li>
        <li><svg viewBox="0 0 16 14"><path d="M1 7l5 5L15 1" fill="none" stroke="#a89a6c" stroke-width="2.4"/></svg>Ensure the contract is <b>guaranteed to be renewed</b> if you pay your premiums until expiry age.</li>
        <li><svg viewBox="0 0 16 14"><path d="M1 7l5 5L15 1" fill="none" stroke="#a89a6c" stroke-width="2.4"/></svg>If purchased through Super, <b>you may be liable for a tax bill</b> in the event of a claim</li>
      </ul>
    </div>
    <div class="board__panel col-right row-2p">
      <p class="panel-copy" style="top:12px">If you need help:</p>
      <ul class="dot-list dot-list--advice">
        <li>Comparing premiums</li>
        <li>Reviewing &amp; comparing policy terms and conditions</li>
        <li>Matching a policy to suit your occupation</li>
        <li>Purchasing “Long Term” Life Insurance</li>
      </ul>
      <p class="panel-copy" style="top:190px">If you want to ensure that you have someone assisting you if a claim is ever needed to be made</p>
    </div>
  </div>
  <p class="disclaimer">The information provided on this Fact Sheet is <b>general advice only</b> so does <b>not</b> take into account your objective, financial situation and needs. Before acting on any information contained on this Fact Sheet you should consider the appropriateness of the advice having regard to your own objectives, financial situation and needs.</p>
  <div class="brand"><span class="brand__mark"></span>HALVARD MENSLEY<br>FINANCIAL SERVICES</div>
</section>

<section class="sheet sheet--thumb sheet--income">
  <h1 class="sheet__title">Buying Income Protection Insurance</h1>
  <div class="banner">
    <div class="banner__photo" role="img" aria-label="Photo of fanned banknotes" style="background:linear-gradient(90deg,#6aa2b8 0%,#d9c46a 30%,#c2556b 55%,#e3a24a 80%,#8fb6c9 100%)"></div>
  </div>
  <div class="board">
    <div class="board__head col-left row-1h">How Much Do I Need?</div>
    <div class="board__head col-right row-1h">Who Offers It?</div>
    <div class="board__panel col-left row-1p">
      <p class="panel-copy" style="top:40px;text-align:justify">Most people insure 75% of their income, which is the maximum benefit that Insurance Companies generally cover.</p>
    </div>
    <div class="board__panel col-right row-1p">
      <ul class="dot-list">
        <li>Most Superannuation Funds</li>
        <li>Some Private Health Funds</li>
        <li>Some Employers</li>
        <li>Life Insurance Companies</li>
        <li>General Insurance Companies</li>
      </ul>
    </div>
    <div class="board__head col-left row-2h">Tips and Traps</div>
    <div class="board__head col-right row-2h">When to Call a Professional Advisor?</div>
    <div class="board__panel col-left row-2p">
      <ul class="tick-list">
        <li><svg viewBox="0 0 16 14"><path d="M1 7l5 5L15 1" fill="none" stroke="#a89a6c" stroke-width="2.4"/></svg>Ensure Policy <b>covers all illnesses and injuries</b>, not just accidents.</li>
        <li><svg viewBox="0 0 16 14"><path d="M1 7l5 5L15 1" fill="none" stroke="#a89a6c" stroke-width="2.4"/></svg><b>Review what the policy doesn't cover "Exclusions"</b>. Standard exclusions include self-inflicted acts, pregnancy related illnesses and war related claims.</li>
        <li><svg viewBox="0 0 16 14"><path d="M1 7l5 5L15 1" fill="none" stroke="#a89a6c" stroke-width="2.4"/></svg><b>Understand the definitions of "Total and Partial Disability"</b> so you know when you can make a claim.</li>
        <li><svg viewBox="0 0 16 14"><path d="M1 7l5 5L15 1" fill="none" stroke="#a89a6c" stroke-width="2.4"/></svg>Look to <b>purchase "Long Term" Life Insurance</b> if you think you will need to hold the policy for a number of years. This may save you tens of thousands of dollars over the life of your policy.</li>
        <li><svg viewBox="0 0 16 14"><path d="M1 7l5 5L15 1" fill="none" stroke="#a89a6c" stroke-width="2.4"/></svg>Ensure the contract is <b>guaranteed to be renewed</b> if you pay your premiums until expiry age.</li>
        <li><svg viewBox="0 0 16 14"><path d="M1 7l5 5L15 1" fill="none" stroke="#a89a6c" stroke-width="2.4"/></svg>Paying the premiums yourself, will generally enable you to <b>claim a tax deduction</b></li>
      </ul>
    </div>
    <div class="board__panel col-right row-2p">
      <p class="panel-copy" style="top:12px">If you need help:</p>
      <ul class="dot-list dot-list--advice">
        <li>Comparing premiums</li>
        <li>Reviewing &amp; comparing policy terms and conditions</li>
        <li>Matching a policy to suit your occupation</li>
        <li>Deciding on the appropriate Waiting Periods and Benefit Periods</li>
        <li>Purchasing “Long Term” Life Insurance</li>
      </ul>
      <p class="panel-copy" style="top:212px">If you want to ensure that you have someone assisting you if a claim is ever needed to be made.</p>
      <p class="panel-copy" style="top:270px">If your financial affairs are complex due to being self employed or a high income earner.</p>
    </div>
  </div>
  <p class="disclaimer">The information provided on this Fact Sheet is <b>general advice only</b> so does <b>not</b> take into account your objective, financial situation and needs. Before acting on any information contained on this Fact Sheet you should consider the appropriateness of the advice having regard to your own objectives, financial situation and needs.</p>
  <div class="brand"><span class="brand__mark"></span>HALVARD MENSLEY<br>FINANCIAL SERVICES</div>
</section>

<section class="sheet sheet--thumb sheet--critical">
  <h1 class="sheet__title">Buying Critical Illness Insurance</h1>
  <div class="banner">
    <div class="banner__photo" role="img" aria-label="Photo of a doctor in a white coat with a stethoscope" style="background:linear-gradient(90deg,#f4f4f4 0%,#d7dbe0 35%,#3d4a60 55%,#eef0f3 75%,#ffffff 100%)"></div>
  </div>
  <div class="board">
    <div class="board__head col-left row-1h">How Much Do I Need?</div>
    <div class="board__head col-right row-1h">Who Offers It?</div>
    <div class="board__panel col-left row-1p">
      <table class="need-table">
        <tr><th>Need</th><th>Amount</th></tr>
        <tr><td>Medical Expenses</td><td class="amount">$</td></tr>
        <tr><td>Others</td><td class="amount">$</td></tr>
        <tr class="total"><td>Total</td><td class="amount">$</td></tr>
      </table>
    </div>
    <div class="board__panel col-right row-1p">
      <ul class="dot-list" style="top:20px">
        <li>Some Private Health Funds</li>
        <li>Some Employers</li>
        <li>Life Insurance Companies</li>
        <li>General Insurance Companies</li>
      </ul>
    </div>
    <div class="board__head col-left row-2h">Tips and Traps</div>
    <div class="board__head col-right row-2h">When to Call a Professional Advisor?</div>
    <div class="board__panel col-left row-2p">
      <ul class="tick-list">
        <li><svg viewBox="0 0 16 14"><path d="M1 7l5 5L15 1" fill="none" stroke="#a89a6c" stroke-width="2.4"/></svg><b>Pay particular attention to the definitions for Cancer and Cardiovascular conditions</b> such as Heart Attack so you are aware of when you can claim.</li>
        <li><svg viewBox="0 0 16 14"><path d="M1 7l5 5L15 1" fill="none" stroke="#a89a6c" stroke-width="2.4"/></svg><b>Review what the policy doesn't cover "Exclusions"</b>. Standard exclusion for most policies is self inflicted acts.</li>
        <li><svg viewBox="0 0 16 14"><path d="M1 7l5 5L15 1" fill="none" stroke="#a89a6c" stroke-width="2.4"/></svg>Look to <b>purchase "Long Term" Life Insurance</b> if you think you will need to hold the policy for a number of years. This may save you tens of thousands of dollars over the life of your policy.</li>
        <li><svg viewBox="0 0 16 14"><path d="M1 7l5 5L15 1" fill="none" stroke="#a89a6c" stroke-width="2.4"/></svg>Ensure the contract is <b>guaranteed to be renewed</b> if you pay your premiums until expiry age.</li>
      </ul>
    </div>
    <div class="board__panel col-right row-2p">
      <p class="panel-copy" style="top:12px">If you need help:</p>
      <ul class="dot-list dot-list--advice">
        <li>Comparing premiums</li>
        <li>Reviewing &amp; comparing policy terms and conditions</li>
        <li>Purchasing “Long Term” Life Insurance</li>
      </ul>
      <p class="panel-copy" style="top:160px">If you want to ensure that you have someone assisting you if a claim is ever needed to be made.</p>
    </div>
  </div>
  <p class="disclaimer">The information provided on this Fact Sheet is <b>general advice only</b> so does <b>not</b> take into account your objective, financial situation and needs. Before acting on any information contained on this Fact Sheet you should consider the appropriateness of the advice having regard to your own objectives, financial situation and needs.</p>
  <div class="brand"><span class="brand__mark"></span>HALVARD MENSLEY<br>FINANCIAL SERVICES</div>
</section>

</body>
</html>
```